Awesome Beer Labels for food pairing

We are going to launch a range of craft beers specially brewed for food pairing, and we are in need of a logo and bottle labels to represent this. Every label individually has to show which beer type it is and the food groups it matches with. At the same time the whole range has to have the same appearance as we are promoting it as a whole package. As we are targeting middle-high to high class hospitality businesses we are looking for a luxurious, exclusive feel to the labels. We also need room for a clear title of the beer and a small food pairing description.

Industry/Entity Type

Craft Brewery

Font styles to use
Sans Serif
Decorative
Script

Colors

Designer to choose colors to be used in the design.

Requirements
Must have
• -Different beer labels where the style and name of the beer comes first, and the beer type second
• - A logo for the whole group which also has to be printed on glasses, so nothing to detailed.
• - Clear, recognizable pictures, drawings or symbols for the different food groups.
• - Room for the name of the beer, the beer type and a small description.
Nice to have
• An exclusive, luxurious look and feel that would not stand out in an high class restaurant.
• Something that combines the whole range of beers (something like a overlaying or connecting picture that combines alle the labels?)
Should not have
• To much different styles, the beers have to match

```html
<!DOCTYPE html>
<html lang="en">
<head>
<meta charset="utf-8">
<title>Pale Lager – Bottle Label</title>
<link rel="stylesheet" href="https://fonts.googleapis.com/css2?family=Arvo:wght@700&family=Josefin+Sans:wght@300&family=Oswald:wght@400&family=Open+Sans:wght@500&family=UnifrakturMaguntia&display=swap">
<style>
  :root {
    --backdrop-light: #f2f2f2;
    --backdrop-dark: #d9d9d9;
    --label-blue: #2234b8;
    --label-blue-light: #3248d6;
    --label-blue-deep: #17238a;
    --ink: #ffffff;
    --emblem-tone: #4a5fdc;
  }
  html, body {
    margin: 0;
    padding: 0;
    width: 857px;
    height: 1200px;
    overflow: hidden;
  }
  body {
    background: radial-gradient(ellipse at 50% 40%, var(--backdrop-light), var(--backdrop-dark));
    position: relative;
  }
  .label {
    position: absolute;
    left: 128px;
    top: 192px;
    width: 600px;
    height: 815px;
    background: linear-gradient(100deg, var(--label-blue-deep) 0%, var(--label-blue-light) 35%, var(--label-blue) 70%, var(--label-blue-deep) 100%);
    color: var(--ink);
  }
  .label-lines {
    position: absolute;
    inset: 0;
  }
  .title-box {
    position: absolute;
    left: 138px;
    top: 21px;
    width: 309px;
    height: 192px;
    box-sizing: border-box;
    border: 3px solid var(--ink);
    background: linear-gradient(100deg, var(--label-blue-light), var(--label-blue));
    text-align: center;
  }
  .title-style {
    height: 95px;
    border-bottom: 3px solid var(--ink);
    margin: 0 14px;
    font-family: "Josefin Sans", sans-serif;
    font-weight: 300;
    font-size: 62px;
    letter-spacing: 16px;
    line-height: 104px;
    padding-left: 16px;
  }
  .title-type {
    font-family: "Arvo", serif;
    font-weight: 700;
    font-size: 52px;
    letter-spacing: 6px;
    line-height: 90px;
  }
  .volume, .strength {
    position: absolute;
    font-family: "Oswald", sans-serif;
    font-weight: 400;
    line-height: 1;
    text-align: center;
  }
  .volume {
    left: 50px;
    top: 180px;
    font-size: 46px;
    letter-spacing: -1px;
  }
  .strength {
    left: 476px;
    top: 160px;
    font-size: 42px;
    line-height: 46px;
  }
  .emblem {
    position: absolute;
    left: 160px;
    top: 248px;
    width: 270px;
    height: 180px;
    border-radius: 90px 90px 40px 40px;
    background: radial-gradient(ellipse at 50% 40%, var(--emblem-tone), var(--label-blue));
  }
  .description {
    position: absolute;
    left: 70px;
    top: 462px;
    width: 444px;
    margin: 0;
    font-family: "Open Sans", sans-serif;
    font-weight: 500;
    font-size: 19.5px;
    line-height: 23px;
    text-align: center;
  }
  .pairing-ribbon {
    position: absolute;
    left: 120px;
    top: 598px;
    width: 346px;
    height: 80px;
  }
  .pairing-ribbon text {
    font-family: "UnifrakturMaguntia", serif;
    font-size: 23px;
    fill: var(--label-blue);
  }
  .pairing-food {
    position: absolute;
    left: 196px;
    top: 664px;
    width: 186px;
    height: 86px;
    border-radius: 50%;
    background: linear-gradient(90deg, var(--emblem-tone), var(--label-blue-light));
  }
</style>
</head>
<body>
  <main class="label">
    <svg class="label-lines" width="600" height="815" viewBox="0 0 600 815" aria-hidden="true">
      <g fill="none" stroke="#ffffff" stroke-width="3">
        <rect class="outer-frame" x="25" y="111" width="539" height="679"/>
        <polyline class="inner-frame" points="160,299 56,299 56,763 533,763 533,299 430,299"/>
      </g>
    </svg>

    <header class="title-box">
      <div class="title-style">PALE</div>
      <div class="title-type">LAGER</div>
    </header>

    <div class="volume">33cl</div>
    <div class="strength">5%<br>alc</div>

    <div class="emblem" role="img" aria-label="Emblem: beer mug framed by a wheat laurel with a star below"></div>

    <p class="description">Lorem ipsum dolor sit amet,<br>consectetuer adipiscing elit, sed<br>diam nonummy nibh euismod tinci-<br>dunt ut laoreet dolore magna ali-<br>quam erat volutpat. Ut wisi enim</p>

    <svg class="pairing-ribbon" viewBox="0 0 346 80" aria-label="Pairing banner">
      <path d="M20,62 Q173,10 326,62 L326,36 Q173,-16 20,36 Z" fill="#ffffff"/>
      <path id="ribbon-curve" d="M34,54 Q173,8 312,54" fill="none"/>
      <text><textPath href="#ribbon-curve" startOffset="50%" text-anchor="middle">best assortment with fish</textPath></text>
    </svg>

    <div class="pairing-food" role="img" aria-label="Fish icon marking the food pairing"></div>
  </main>
</body>
</html>
```